Create a new dynamic Video Production company website

A new website for a video production company. It needs to be focused on the videos with an easy to use and versatile video player. I want to be able to update (add/remove/edit) the videos myself and change some other regular information like price lists. Current website is www.reelvanta.ca
The new pages will be - Home - Corporate - Ministry - Wedding - Events - Contact

I was asked about Wordpress - I am not against WordPress so long as the designing company sets everything up properly. I have had bad experiences with Wordpress security (and spam) so as long as those issues are addressed, I can work with Wordpress.

Requirements
Must have
• Video player that scales to different platforms - computers, tablets, cell phones etc.

```html
<!DOCTYPE html>
<html lang="en">
<head>
<meta charset="utf-8">
<title>Reelvanta – Video Production</title>
<link href="https://fonts.googleapis.com/css2?family=Rubik:wght@300;400;500;700&display=swap" rel="stylesheet">
<style>
:root{
  --page:#ffffff;
  --ink:#1e1e1e;
  --muted:#7a7a7a;
  --name:#5a5a5a;
  --white:#ffffff;
  --hero-dark:#2f3a40;
  --hero-sky:#6d7f88;
  --hero-sand:#9a8f85;
  --accent:#b4563a;
  --accent-dark:#983e24;
  --footer:#3a3a3a;
}
*{box-sizing:border-box;margin:0;padding:0}
html,body{width:1200px;height:1200px;overflow:hidden;background:var(--page)}
body{font-family:'Rubik',sans-serif;position:relative}
.site{position:absolute;left:213px;top:0;width:777px;height:1196px;background:var(--page)}

/* hero */
.hero{position:absolute;left:0;top:0;width:777px;height:438px;overflow:hidden}
.hero-photo{position:absolute;inset:0;background:
  linear-gradient(180deg,var(--hero-sky) 0%,var(--hero-dark) 42%,var(--hero-sand) 100%)}
.hero-shade{position:absolute;inset:0;background:rgba(20,26,30,.45)}
.brand{position:absolute;left:53px;top:14px;font-weight:500;font-size:20px;letter-spacing:1px;color:var(--white)}
.nav{position:absolute;right:51px;top:19px;display:flex;gap:13px}
.nav a{font-size:10.5px;font-weight:500;color:var(--white);text-decoration:none;letter-spacing:.1px}
.hero-title{position:absolute;left:0;width:100%;top:138px;text-align:center;font-weight:300;font-size:42px;color:var(--white)}
.hero-lead{position:absolute;left:0;width:100%;top:196px;text-align:center;font-weight:300;font-size:15px;line-height:24px;color:var(--white)}
.btn{position:absolute;top:257px;height:33px;border-radius:17px;background:var(--white);color:var(--ink);
  font-size:10.5px;font-weight:500;letter-spacing:1px;display:flex;align-items:center;justify-content:center}
.btn-about{left:259px;width:131px}
.btn-services{left:406px;width:120px}
.slider-arrow{position:absolute;top:204px}
.slider-arrow.prev{left:26px}
.slider-arrow.next{left:714px}
.slider-dots{position:absolute;top:408px;left:353px}

/* testimonials */
.section-title{position:absolute;top:494px;left:0;width:100%;text-align:center;font-weight:300;font-size:37px;color:var(--ink);letter-spacing:.3px}
.testimonial{position:absolute;top:630px;width:160px;text-align:center}
.testimonial.t1{left:69px}
.testimonial.t2{left:316px}
.testimonial.t3{left:563px}
.avatar{width:96px;height:96px;border-radius:50%;margin:0 auto 21px}
.avatar.a1{background:radial-gradient(circle at 50% 45%,#c9a493 0 38%,#3b2922 60%)}
.avatar.a2{background:radial-gradient(circle at 50% 50%,#e2b8a6 0 40%,#5a3325 65%)}
.avatar.a3{background:radial-gradient(circle at 50% 50%,#dcb49a 0 40%,#8a6b3e 65%)}
.quote{font-size:12.5px;font-weight:300;line-height:20px;color:var(--muted)}
.author{margin-top:14px;font-size:12.5px;font-weight:500;color:var(--name)}

/* contact band */
.contact-band{position:absolute;left:0;top:958px;width:777px;height:171px;overflow:hidden}
.contact-photo{position:absolute;inset:0;background:linear-gradient(100deg,var(--accent) 0%,#bd6448 45%,var(--accent-dark) 100%)}
.mail-btn{position:absolute;left:90px;top:68px;width:166px;height:53px;border:2px solid var(--white);border-radius:27px;
  display:flex;align-items:center;justify-content:center;gap:14px;color:var(--white)}
.mail-btn span{font-size:12px;font-weight:500;letter-spacing:1px;text-align:center;line-height:13px}
.contact-copy{position:absolute;right:74px;top:57px;text-align:right;color:var(--white)}
.contact-copy h2{font-size:19px;font-weight:700;margin-bottom:14px}
.contact-copy p{font-size:12.5px;font-weight:300;line-height:16px}
.contact-copy strong{font-weight:700}

.site-footer{position:absolute;left:0;top:1129px;width:777px;height:67px;background:var(--footer);
  color:var(--white);font-size:12.5px;font-weight:300;display:flex;align-items:center;justify-content:center}
</style>
</head>
<body>
<div class="site">
  <header class="hero">
    <div class="hero-photo" role="img" aria-label="Hands holding a film clapperboard against a desert sky"></div>
    <div class="hero-shade"></div>
    <div class="brand">REELVANTA</div>
    <nav class="nav">
      <a href="#">HOME</a><a href="#">CORPORATE</a><a href="#">MINISTERY</a><a href="#">WEDDING</a><a href="#">EVENTS</a><a href="#">CONTACTS</a>
    </nav>
    <h1 class="hero-title">Video Production</h1>
    <p class="hero-lead">We create unique and original video productions for your Business.<br>Allow us to bring your thoughts, ideas and dreams, into a custom video production.</p>
    <a class="btn btn-about">ABOUT US...</a>
    <a class="btn btn-services">SERVICES</a>
    <svg class="slider-arrow prev" width="46" height="46" viewBox="0 0 46 46"><circle cx="23" cy="23" r="22" fill="none" stroke="#fff" stroke-opacity=".7" stroke-width="1.2"/><path d="M32 23H14M21 16l-7 7 7 7" fill="none" stroke="#fff" stroke-width="1.3"/></svg>
    <svg class="slider-arrow next" width="46" height="46" viewBox="0 0 46 46"><circle cx="23" cy="23" r="22" fill="none" stroke="#fff" stroke-opacity=".7" stroke-width="1.2"/><path d="M14 23h18M25 16l7 7-7 7" fill="none" stroke="#fff" stroke-width="1.3"/></svg>
    <svg class="slider-dots" width="80" height="14" viewBox="0 0 80 14">
      <circle cx="7" cy="7" r="5.5" fill="none" stroke="#fff" stroke-width="1.3"/>
      <circle cx="24" cy="7" r="5.5" fill="none" stroke="#fff" stroke-opacity=".7" stroke-width="1.2"/>
      <circle cx="41" cy="7" r="5.5" fill="none" stroke="#fff" stroke-opacity=".7" stroke-width="1.2"/>
      <circle cx="58" cy="7" r="5.5" fill="none" stroke="#fff" stroke-opacity=".7" stroke-width="1.2"/>
      <circle cx="75" cy="7" r="5.5" fill="none" stroke="#fff" stroke-opacity=".7" stroke-width="1.2"/>
    </svg>
  </header>

  <h2 class="section-title">WHAT OUR FANTASTIC CUSTOMERS SAY</h2>

  <article class="testimonial t1">
    <div class="avatar a1" role="img" aria-label="Portrait of customer Mira Dalton"></div>
    <p class="quote">The photos of my wedding were simply fantastic. I sincerely recommend Reelvanta</p>
    <p class="author">Mira Dalton</p>
  </article>
  <article class="testimonial t2">
    <div class="avatar a2" role="img" aria-label="Portrait of customer Lena Varga"></div>
    <p class="quote">The image of the company is what defines its position in the market. We trust Reelvanta</p>
    <p class="author">Lena Varga</p>
  </article>
  <article class="testimonial t3">
    <div class="avatar a3" role="img" aria-label="Portrait of customer Nora Hale"></div>
    <p class="quote">My pregnancy and the birth of my first child are moments recorded by Reelvanta. Thanks for the quality</p>
    <p class="author">Nora Hale</p>
  </article>

  <section class="contact-band">
    <div class="contact-photo" role="img" aria-label="Blurred hands typing on a laptop, tinted orange"></div>
    <a class="mail-btn">
      <svg width="22" height="15" viewBox="0 0 22 15"><rect x="0" y="0" width="22" height="15" fill="#fff"/><path d="M0 0l11 8L22 0" fill="none" stroke="#b4563a" stroke-width="1.6"/></svg>
      <span>E-MAIL<br>US</span>
    </a>
    <div class="contact-copy">
      <h2>Contact us for more details and pricing.</h2>
      <p>E-mail: <strong>contact@reelvanta.ca</strong></p>
      <p>Phone:<strong>519-555-0148</strong></p>
    </div>
  </section>

  <footer class="site-footer">© Copyright 2017 reelvanta - All Rights Reserved</footer>
</div>
</body>
</html>
```